Mobile Design for app

Quill Harbor mobile design - This design is specifically for Wren42 who has already done the work based on previous canceled project and will be paid based on this projected as soon as it is approved.

***NO DESIGNS NEED TO BE SUBMITTED BY OTHER DESIGNERS FOR THIS PROJECT***

```html
<!DOCTYPE html>
<html lang="en">
<head>
<meta charset="utf-8">
<title>Exam details</title>
<link href="https://fonts.googleapis.com/css2?family=Source+Sans+3:wght@400;600&display=swap" rel="stylesheet">
<style>
  :root {
    --teal-bar: #6aafbc;
    --teal-text: #4e939d;
    --teal-dot: #5a969e;
    --slate: #58595b;
    --grey-tab: #bcbec0;
    --answer-bg: #f1f1f1;
    --ink: #333333;
    --white: #ffffff;
  }
  * { margin: 0; padding: 0; box-sizing: border-box; }
  html, body { width: 675px; height: 1200px; overflow: hidden; background: var(--white); }
  body { font-family: "Source Sans 3", "Source Sans Pro", sans-serif; color: var(--ink); position: relative; }

  .app-top { position: absolute; left: 0; top: 0; width: 675px; height: 121px; background: var(--teal-bar); color: var(--white); }
  .status-bar { position: absolute; left: 0; top: 0; width: 100%; height: 40px; font-size: 19px; color: #3c5f66; }
  .status-bar span { position: absolute; top: 8px; }
  .status-network { left: 10px; }
  .status-clock { left: 0; right: 0; text-align: center; }
  .status-battery { right: 10px; }
  .menu-icon { position: absolute; left: 18px; top: 67px; }
  .screen-title { position: absolute; left: 0; right: 0; top: 60px; text-align: center; font-size: 31px; }

  .timer-panel { position: absolute; left: 0; top: 121px; width: 675px; height: 220px; background: var(--slate); color: var(--white); }
  .time-remaining { position: absolute; left: 16px; top: 13px; font-size: 31px; }
  .collapse-tab { position: absolute; left: 428px; top: 0; width: 247px; height: 67px; background: var(--grey-tab); color: #2b2b2b; font-size: 31px; text-align: center; line-height: 67px; }
  .stat { position: absolute; top: 82px; width: 220px; text-align: center; }
  .stat-value { font-size: 46px; line-height: 56px; }
  .stat-value small { font-size: 30px; }
  .stat-label { font-size: 20px; line-height: 27px; margin-top: 20px; }
  .stat-total { left: -25px; }
  .stat-elapsed { left: 224px; }
  .stat-per { left: 472px; }

  .question { position: absolute; left: 72px; top: 388px; width: 560px; }
  .question-head { display: flex; align-items: center; gap: 28px; color: var(--teal-text); font-size: 31px; height: 44px; }
  .question-body { font-size: 25px; line-height: 34px; margin-top: 4px; }
  .question-body p { margin-bottom: 28px; }
  .question-body p span { display: block; white-space: nowrap; }
  .question-body .lead { font-weight: 600; }

  .answers { position: absolute; left: 48px; top: 938px; width: 577px; list-style: none; }
  .answer { height: 50px; background: var(--answer-bg); display: flex; align-items: center; font-size: 25px; margin-bottom: 18.5px; }
  .answer svg { margin-left: 24px; margin-right: 19px; }
</style>
</head>
<body>
  <header class="app-top">
    <div class="status-bar">
      <span class="status-network">Network</span>
      <span class="status-clock">12:34 PM</span>
      <span class="status-battery">100%</span>
    </div>
    <svg class="menu-icon" width="46" height="30" viewBox="0 0 46 30" aria-hidden="true">
      <g stroke="#ffffff" stroke-width="2" fill="none">
        <rect x="1" y="1" width="44" height="4"/>
        <rect x="1" y="9" width="44" height="4"/>
        <rect x="1" y="17" width="44" height="4"/>
        <rect x="1" y="25" width="44" height="4"/>
      </g>
    </svg>
    <h1 class="screen-title" style="font-weight:400">Exam details</h1>
  </header>

  <section class="timer-panel">
    <div class="time-remaining">Time remaining 21:59</div>
    <div class="collapse-tab">Collapse&lt;</div>
    <div class="stat stat-total"><div class="stat-value">15 <small>min</small></div><div class="stat-label">Total<br>Time</div></div>
    <div class="stat stat-elapsed"><div class="stat-value">05:15</div><div class="stat-label">Elapsed<br>Time</div></div>
    <div class="stat stat-per"><div class="stat-value">1 <small>min</small></div><div class="stat-label">Time per<br>Question</div></div>
  </section>

  <article class="question">
    <div class="question-head">
      <span>Question 05</span>
      <svg width="36" height="36" viewBox="0 0 36 36" aria-hidden="true"><circle cx="18" cy="18" r="16" fill="none" stroke="#4e939d" stroke-width="2.5"/></svg>
    </div>
    <div class="question-body">
      <p>
        <span>Lorem ipsum dolor sit amet, consectetur</span>
        <span>adipisicing elit, sed do eiusmod tempor incid-</span>
        <span>idunt ut labore et dolore magna aliqua. Ut</span>
        <span>enim ad minim veniam, quis nostrud exercita-</span>
        <span>tion ullamco laboris nisi ut aliquip ex ea com-</span>
      </p>
      <p class="lead">
        <span>Lorem ipsum dolor sit amet, consectetur</span>
        <span>adipisicing elit, sed do eiusmod tempor inci-</span>
      </p>
      <p>
        <span>Lorem ipsum dolor sit amet, consectetur</span>
        <span>adipisicing elit, sed do eiusmod tempor incid-</span>
        <span>idunt ut labore et dolore magna aliqua. Ut</span>
      </p>
    </div>
  </article>

  <ul class="answers">
    <li class="answer"><svg width="38" height="38" viewBox="0 0 38 38" aria-hidden="true"><circle cx="19" cy="19" r="17" fill="none" stroke="#5a969e" stroke-width="2.5"/></svg>Answer One is here</li>
    <li class="answer"><svg width="38" height="38" viewBox="0 0 38 38" aria-hidden="true"><circle cx="19" cy="19" r="18" fill="#5a969e"/></svg>Answer Two</li>
    <li class="answer"><svg width="38" height="38" viewBox="0 0 38 38" aria-hidden="true"><circle cx="19" cy="19" r="17" fill="none" stroke="#5a969e" stroke-width="2.5"/></svg>Answer Three</li>
    <li class="answer"><svg width="38" height="38" viewBox="0 0 38 38" aria-hidden="true"><circle cx="19" cy="19" r="17" fill="none" stroke="#5a969e" stroke-width="2.5"/></svg>Next answer</li>
  </ul>
</body>
</html>
```